Criação de Logo + Papelaria + Manual Básico para Ventrona & Solmar
" Atendemos os clientes de forma consultiva, procurando no mercado as tecnologias mais adequadas para a otimização e estabilidade de redes corporativas. Somos parceiros homologados dos principais fabricantes do mercado, além de mantermos parcerias estratégicas para complementar nossas soluções com todas as competências necessárias. "

```html
<!DOCTYPE html>
<html lang="pt-BR">
<head>
<meta charset="utf-8">
<title>Ventrona &amp; Solmar — Pasta</title>
<link rel="stylesheet" href="https://fonts.googleapis.com/css2?family=Exo+2:wght@500;600&family=Montserrat:wght@500&display=swap">
<style>
  :root{
    --stage:#e8e9eb;
    --navy:#13202b;
    --paper:#ffffff;
    --teal:#1aa8c3;
    --ink:#2b3a48;
    --mark-faint:#eef1f4;
    --mark-faint-dark:#1a2935;
    --contact:#c9d3dc;
  }
  *{margin:0;padding:0;box-sizing:border-box}
  html,body{width:1200px;height:1200px;overflow:hidden;background:var(--stage)}
  .canvas{position:relative;width:1200px;height:1200px}
  .folder-back{position:absolute;left:72px;top:125px;width:547px;height:864px;background:var(--navy);overflow:hidden}
  .folder-front{position:absolute;left:619px;top:125px;width:509px;height:864px;background:var(--paper);overflow:hidden;box-shadow:2px 4px 14px rgba(0,0,0,.08)}
  .brand{font-family:"Exo 2",sans-serif;font-weight:600;text-align:center;position:absolute;left:0;right:0;letter-spacing:.5px}
  .brand-back{top:100px;color:var(--paper);font-size:26px}
  .brand-front{top:340px;color:var(--ink);font-size:40px}
  .brand-dot{display:block;margin:0 auto 12px;border-radius:50%;background:var(--teal)}
  .brand-back .brand-dot{width:30px;height:30px}
  .brand-front .brand-dot{width:44px;height:44px}
  .faint-mark{position:absolute;font-family:"Exo 2",sans-serif;font-weight:600;white-space:nowrap;line-height:1}
  .faint-mark-front{left:-60px;top:320px;font-size:150px;color:var(--mark-faint)}
  .faint-mark-back{left:460px;top:320px;font-size:150px;color:var(--mark-faint-dark)}
  .contact{position:absolute;left:0;right:0;top:700px;font-family:"Montserrat",sans-serif;font-weight:500;font-size:10px;color:var(--contact);display:flex;flex-direction:column;align-items:center;gap:6px}
  .contact-row{display:flex;gap:14px;align-items:center}
  .contact-item{display:flex;align-items:center;gap:4px}
  .contact-item svg{width:10px;height:10px;fill:var(--contact)}
  .pocket{position:absolute;left:0;top:0;width:1200px;height:1200px;pointer-events:none}
</style>
</head>
<body>
<div class="canvas">
  <section class="folder-back">
    <div class="faint-mark faint-mark-back">Ventrona &amp; Solmar</div>
    <div class="brand brand-back"><span class="brand-dot"></span>Ventrona &amp; Solmar</div>
    <div class="contact">
      <div class="contact-row">
        <span class="contact-item"><svg viewBox="0 0 10 10"><path d="M2 0.5l2 2-1 1.2c.6 1.3 1.6 2.3 2.9 2.9l1.2-1 2 2-1.3 1.6C4.5 9.2 0.8 5.5 0.5 1.8z"/></svg>+55 27 4310-5521</span>
        <span class="contact-item"><svg viewBox="0 0 10 10"><path d="M2 0.5l2 2-1 1.2c.6 1.3 1.6 2.3 2.9 2.9l1.2-1 2 2-1.3 1.6C4.5 9.2 0.8 5.5 0.5 1.8z"/></svg>+55 27 4310-5522</span>
      </div>
      <div class="contact-row">
        <span class="contact-item"><svg viewBox="0 0 10 10"><path d="M0 2h10v6H0z M0 2l5 3.5L10 2" /></svg>ola@ventronasolmar.com</span>
        <span class="contact-item"><svg viewBox="0 0 10 10"><circle cx="5" cy="5" r="4.5"/></svg>www.ventronasolmar.com</span>
      </div>
      <div class="contact-row">
        <span class="contact-item"><svg viewBox="0 0 10 10"><path d="M5 0a3.5 3.5 0 0 1 3.5 3.5C8.5 6 5 10 5 10S1.5 6 1.5 3.5A3.5 3.5 0 0 1 5 0z"/></svg>Rua das Palmeiras, 214</span>
      </div>
    </div>
  </section>

  <section class="folder-front">
    <div class="faint-mark faint-mark-front">Ventrona &amp; Solmar</div>
    <div class="brand brand-front"><span class="brand-dot"></span>Ventrona &amp; Solmar</div>
  </section>

  <svg class="pocket" viewBox="0 0 1200 1200" aria-hidden="true">
    <path fill="var(--teal)" d="M48 830 C48 812 60 806 80 806 L560 806 C590 806 600 830 619 845 L619 1075 L48 1075 Z"/>
  </svg>
</div>
</body>
</html>
```